Poster of Insipirational Quotes

Attached is a list of leadership quotes from Arlen Drubeck. I would like a poster made, incorporating whatever design elements you like, potentially including Arlen's face, and one or more of the quotes. I intend to print this out in A3 or larger to hang on my wall.

The quotes are:

Being responsible sometimes means pissing people off.

The day soldiers stop bringing you their problems is the day you have stopped leading them.

Don't be buffaloed by experts and elites. Experts often possess more data than judgment. Elites can become so inbred that they produce hemophiliacs who bleed to death as soon as they are nicked by the real world.

Don't be afraid to challenge the pros, even in their own backyard.

Never neglect details. When everyone's mind is dulled or distracted the leader must be doubly vigilant.

You don't know what you can get away with until you try.

Keep looking below surface appearances. Don't shrink from doing so (just) because you might not like what you find.

Organization doesn't really accomplish anything. Plans don't accomplish anything, either. Theories of management don't much matter. Endeavors succeed or fail because of the people involved. Only by attracting the best people will you accomplish great deeds.

Organization charts and fancy titles count for next to nothing.

Never let your ego get so close to your position that when your position goes, your ego goes with it.

Fit no stereotypes. Don't chase the latest management fads. The situation dictates which approach best accomplishes the team's mission.

Perpetual optimism is a force multiplier.

Look for intelligence and judgment, and most critically, a capacity to anticipate, to see around corners. Also look for loyalty, integrity, a high energy drive, a balanced ego, and the drive to get things done.

Great leaders are almost always great simplifiers, who can cut through argument, debate and doubt, to offer a solution everybody can understand.

The commander in the field is always right and the rear echelon is wrong, unless proved otherwise.

Have fun in your command. Don't always run at a breakneck pace. Take leave when you've earned it: Spend time with your families. Corollary: surround yourself with people who take their work seriously, but not themselves, those who work hard and play hard.

Command is lonely.

Leadership is the art of accomplishing more than the science of management
says is possible.
Updates

I need to modify the specification based on the designs that I've seen.

Target Market(s)

Executive Office

Colors

Designer to choose colors to be used in the design.

Requirements
Must have
• Quotes

```html
<!DOCTYPE html>
<html lang="en">
<head>
<meta charset="utf-8">
<title>Leadership Quotes – Arlen Drubeck</title>
<link href="https://fonts.googleapis.com/css2?family=Bebas+Neue&family=Roboto+Condensed:ital,wght@1,700&display=swap" rel="stylesheet">
<style>
  :root {
    --backdrop: #e4e4e4;
    --paper: #ffffff;
    --ink: #1b1b1b;
    --portrait-light: #f1f1f3;
    --portrait-mid: #dcdce0;
  }
  * { margin: 0; padding: 0; box-sizing: border-box; }
  html, body {
    width: 1180px;
    height: 1200px;
    overflow: hidden;
    background: var(--backdrop);
  }
  .poster {
    position: absolute;
    left: 182px;
    top: 16px;
    width: 816px;
    height: 1168px;
    background: var(--paper);
    overflow: hidden;
    color: var(--ink);
  }
  .portrait {
    position: absolute;
    left: 0;
    top: 0;
    width: 816px;
    height: 1168px;
  }
  .frame {
    position: absolute;
    left: 93px;
    top: 82px;
    width: 631px;
    height: 998px;
    border: 10px solid var(--ink);
  }
  .headline, .footline {
    position: absolute;
    font-family: "Bebas Neue", "Arial Narrow", sans-serif;
    font-size: 19px;
    letter-spacing: 0.2px;
    white-space: nowrap;
  }
  .headline {
    left: 81px;
    width: 660px;
    top: 53px;
    text-align: center;
  }
  .footline {
    left: 83px;
    width: 657px;
    top: 1090px;
    display: flex;
    justify-content: space-between;
  }
  .quotes {
    position: absolute;
    left: 186px;
    top: 204px;
    width: 445px;
    font-family: "Bebas Neue", "Arial Narrow", sans-serif;
    font-size: 15.5px;
    line-height: 21px;
    text-align: center;
    letter-spacing: 0.3px;
  }
  .quotes p { margin-bottom: 21px; }
  .side {
    position: absolute;
    width: 1006px;
    height: 20px;
    top: 570px;
    display: flex;
    justify-content: space-between;
    font-family: "Roboto Condensed", "Arial Narrow", sans-serif;
    font-style: italic;
    font-weight: 700;
    font-size: 13.5px;
    line-height: 20px;
    white-space: nowrap;
  }
  .side-left { left: calc(66px - 503px); transform: rotate(-90deg); }
  .side-right { left: calc(755px - 503px); transform: rotate(90deg); }
</style>
</head>
<body>
  <main class="poster">
    <svg class="portrait" role="img" aria-label="Faint halftone portrait of Arlen Drubeck behind the quotes" viewBox="0 0 816 1168">
      <defs>
        <linearGradient id="portraitTone" x1="0" y1="0" x2="0" y2="1">
          <stop offset="0" stop-color="#ffffff"/>
          <stop offset="0.3" stop-color="#f4f4f6"/>
          <stop offset="1" stop-color="#e2e2e6"/>
        </linearGradient>
      </defs>
      <rect x="0" y="160" width="816" height="1008" fill="url(#portraitTone)"/>
    </svg>

    <p class="headline">The day soldiers stop bringing you their problems is the day you have stopped leading them.</p>

    <div class="frame"></div>

    <section class="quotes">
      <p>Organization charts and fancy titles count for next to nothing.</p>
      <p>Fit no stereotypes. Don't chase the latest management fads. The situation dictates which approach best accomplishes the team's mission.</p>
      <p>Don't be buffaloed by experts and elites. Experts often possess more data than judgment. Elites can become so inbred that they produce hemophiliacs who bleed to death as soon as they are nicked by the real world.</p>
      <p>Never neglect details. When everyone's mind is dulled or distracted the leader must be doubly vigilant.</p>
      <p>Organization doesn't really accomplish anything. Plans don't accomplish anything, either. Theories of management don't much matter. Endeavors succeed or fail because of the people involved. Only by attracting the best people will you accomplish great deeds</p>
      <p>Never let your ego get so close to your position that when your position goes, your ego goes with it.</p>
      <p>Look for intelligence and judgment, and most critically, a capacity to anticipate, to see around corners. Also look for loyalty, integrity, a high energy drive, a balanced ego, and the drive to get things done.</p>
      <p>Great leaders are almost always great simplifiers, who can cut through argument, debate and doubt, to offer a solution everybody can understand.</p>
      <p>Have fun in your command. Don't always run at a breakneck pace. Take leave when you've earned it: spend time with your families. Corollary: surround yourself with people who take their work seriously, but not themselves, those who work hard and play hard.</p>
      <p>Leadership is the art of accomplishing more than the science of management says is possible.</p>
    </section>

    <div class="side side-left">
      <span>You don't know what you can get away with until you try.</span>
      <span>The commander in the field is always right and the rear echelon is wrong, unless proved otherwise.</span>
    </div>

    <div class="side side-right">
      <span>Keep looking below surface appearances. Don't shrink from doing so (just) because you might not like what you find.</span>
      <span>Perpetual optimism is a force multiplier.</span>
    </div>

    <div class="footline">
      <span>Don't be afraid to challenge the pros, even in their own backyard.</span>
      <span>Command is lonely.</span>
    </div>
  </main>
</body>
</html>
```